Construction Company Business Card & Stationary
Brovella Concrete
Construction Company Business Card & Stationary - Construction
Creative Brief
Professional
MARCUS DELWYN JR.
Owner
P.O. Box 482 913 Tamsworth Ridge Lane Alder Falls, OR 97351
MarcusJr@Brovella.com
www.Brovella.com

```html
<!DOCTYPE html>
<html lang="en">
<head>
<meta charset="utf-8">
<title>Brovella Concrete – Business Card</title>
<link href="https://fonts.googleapis.com/css2?family=Roboto+Condensed:wght@400;700&display=swap" rel="stylesheet">
<style>
  :root{
    --backdrop:#3b3431;
    --card-black:#111112;
    --card-black-soft:#1f1f21;
    --card-white:#ffffff;
    --ink-dark:#141414;
    --ink-light:#f2f2f2;
    --ink-muted:#a9a9ab;
    --ink-grey:#555555;
    --rule:#6d6d70;
  }
  *{box-sizing:border-box;margin:0;padding:0}
  html,body{width:1200px;height:715px;overflow:hidden}
  body{
    background:var(--backdrop);
    font-family:"Roboto Condensed",Arial,sans-serif;
    position:relative;
  }
  .card{
    position:absolute;
    top:209px;
    width:520px;height:297px;
    border-radius:3px;
    overflow:hidden;
    box-shadow:0 14px 30px rgba(0,0,0,.45);
  }
  .brand-name{
    font-weight:700;letter-spacing:2px;text-transform:uppercase;line-height:1;white-space:nowrap;
  }
  .tagline{
    font-size:10px;letter-spacing:2.4px;text-transform:uppercase;margin-top:8px;white-space:nowrap;
  }
  /* Back side */
  .card-back{left:50px;background:linear-gradient(160deg,var(--card-black-soft),var(--card-black) 60%)}
  .card-back .brand{position:absolute;left:0;right:0;top:104px;text-align:center}
  .card-back .brand-name{font-size:42px;color:var(--ink-light)}
  .card-back .tagline{color:var(--ink-muted)}
  .card-back .web{
    position:absolute;left:0;right:0;bottom:48px;text-align:center;
    font-size:13px;color:var(--ink-light);letter-spacing:.5px;
  }
  /* Front side */
  .card-front{left:630px;background:var(--card-black)}
  .front-top{
    position:absolute;left:0;top:0;width:100%;height:120px;background:var(--card-white);
    padding:30px 0 0 32px;
  }
  .front-top .brand-name{font-size:36px;color:var(--ink-dark)}
  .front-top .tagline{color:var(--ink-grey);font-size:9px;margin-top:6px}
  .front-bottom{
    position:absolute;left:0;top:120px;width:100%;height:177px;
    background:linear-gradient(170deg,#2a2a2c,var(--card-black) 55%);
    border-top:3px solid var(--rule);
  }
  .person{position:absolute;left:32px;top:14px;color:var(--ink-light)}
  .person-name{font-size:13px;font-weight:700;letter-spacing:1px}
  .person-role{font-size:11px;color:var(--ink-muted);margin-top:1px}
  .contact-list{position:absolute;left:32px;top:58px;list-style:none}
  .contact-list li{
    display:flex;align-items:center;gap:7px;
    font-size:11.5px;color:var(--ink-light);height:19px;
  }
  .contact-list svg{width:11px;height:11px;flex:none}
  .front-web{position:absolute;right:30px;top:14px;font-size:13px;color:var(--ink-light)}
  .address{
    position:absolute;right:30px;bottom:22px;text-align:right;
    font-size:12px;line-height:1.45;color:var(--ink-light);font-style:normal;
  }
</style>
</head>
<body>

<section class="card card-back" aria-label="Card back">
  <div class="brand">
    <div class="brand-name">Brovella Concrete</div>
    <div class="tagline">Solid work is poured into every job</div>
  </div>
  <div class="web">www.Brovella.com</div>
</section>

<section class="card card-front" aria-label="Card front">
  <div class="front-top">
    <div class="brand-name">Brovella Concrete</div>
    <div class="tagline">Solid work is poured into every job</div>
  </div>
  <div class="front-bottom">
    <div class="person">
      <div class="person-name">MARCUS DELWYN JR.</div>
      <div class="person-role">Owner</div>
    </div>
    <ul class="contact-list">
      <li><svg viewBox="0 0 12 12"><path d="M3 1l2 2.5-1.2 1.3a6 6 0 003.4 3.4L8.5 7 11 9l-1 2C5 11 1 7 1 2z" fill="#f2f2f2"/></svg>541-555-0142</li>
      <li><svg viewBox="0 0 12 12"><rect x="3" y="0.5" width="6" height="11" rx="1" fill="#f2f2f2"/><rect x="4" y="2" width="4" height="6.5" fill="#111"/></svg>541-555-0187</li>
      <li><svg viewBox="0 0 12 12"><path d="M6 0.5a4 4 0 00-4 4c0 3 4 7 4 7s4-4 4-7a4 4 0 00-4-4z" fill="#f2f2f2"/><circle cx="6" cy="4.5" r="1.5" fill="#111"/></svg>541-555-0163</li>
      <li><svg viewBox="0 0 12 12"><circle cx="6" cy="6" r="5" fill="#f2f2f2"/></svg>mqdelwyn</li>
      <li><svg viewBox="0 0 12 12"><rect x="0.5" y="2" width="11" height="8" rx="1" fill="#f2f2f2"/><path d="M1 2.5l5 4 5-4" stroke="#111" fill="none"/></svg>MarcusJr@Brovella.com</li>
    </ul>
    <div class="front-web">www.Brovella.com</div>
    <address class="address">P.O. Box 482<br>913 Tamsworth Ridge Lane<br>Alder Falls, OR 97351</address>
  </div>
</section>

</body>
</html>
```